Postcard Design

We are a small day care chain operating out of two adjacent homes. We need a design that illustrates a caring loving environment and focuses on the services we provide, our low weekly rates, and urge the receiver of the postcard to enroll now. Our services are: open 24 hours, Saturday care available, Camera surveillance system, small provider to student ratio, kindergarten preparedness program, tutoring, introduction to Spanish, music, art, gym, after school program, NQBT membership, transportation from and to home, school drop off and pick up, 3 meals and 3 snacks served daily. Our rates: starting as low as $78.22 a week and we accept KVD, employer, and military assistance. Certifications: State of Ohio licensed, Brindle County trained and certified, ZRPA trained. We are offering a wavier on the registration fee and space is limited. We would like are postcards to have the color shades of blue, green and yellow. Contact info: 555 271 9043 call for tour and visit us @ HartwellFamilyDayCare.example and on Facebook @ Hartwell Family Day Care. Location: across from the Delcourt Playhouse. Serving ages 6 weeks to 12 years. These details must be noticeably displayed. Also our name Hartwell Family Day Care must be displayed on both sides.
Updates

We would like for the postcard to highlight our torturing pprogram and to say "ask about NQBT Membership"

Target Market(s)

young (ages 18-35)women with children

Industry/Entity Type

Environment

Requirements
Must have
• personality and character must stand out

```html
<!DOCTYPE html>
<html lang="en">
<head>
<meta charset="utf-8">
<title>Hartwell Family Day Care – Postcard</title>
<link href="https://fonts.googleapis.com/css2?family=Oswald:wght@400;500&family=Roboto:ital,wght@0,400;0,700;0,900;1,700;1,900&family=Quicksand:wght@400&display=swap" rel="stylesheet">
<style>
  :root{
    --bg:#ebebeb;
    --teal:#1e7f9c;
    --teal-dark:#0d4f6e;
    --navy:#0a3a5c;
    --green:#7dc143;
    --yellow:#f7e100;
    --yellow-tag:#f5d90a;
    --blue-text:#1b6fa3;
    --grey-text:#555;
    --white:#ffffff;
  }
  *{box-sizing:border-box;margin:0;padding:0}
  html,body{width:1200px;height:848px;overflow:hidden;background:var(--bg)}
  body{position:relative;font-family:"Roboto",Arial,sans-serif}

  .card{position:absolute;width:538px;height:417px;overflow:hidden;background:var(--white)}
  .card--front{left:56px;top:195px}
  .card--back{left:619px;top:253px}

  /* front */
  .front-photo{position:absolute;left:0;top:0;width:538px;height:220px;
    background:linear-gradient(100deg,#c9b39c 0%,#e8d8c2 35%,#d9b98e 60%,#b7a08a 100%)}
  .front-waves{position:absolute;left:0;top:0}
  .title-panel{position:absolute;left:232px;top:14px;width:306px;height:76px;background:rgba(255,255,255,.88);text-align:center;padding-top:4px}
  .brand{font-family:"Oswald",sans-serif;font-weight:500;color:var(--green);font-size:24px;line-height:30px;letter-spacing:-.2px}
  .tagline{display:flex;align-items:center;justify-content:center;gap:6px;font-family:"Quicksand",sans-serif;font-size:11px;color:var(--grey-text);letter-spacing:.5px}
  .tagline::before,.tagline::after{content:"";height:1px;width:46px;background:#777}
  .ages{font-style:italic;font-weight:900;color:var(--blue-text);font-size:14.5px;margin-top:4px}

  .badge{position:absolute;left:428px;top:113px;width:106px;height:106px;border-radius:50%;background:var(--green);display:flex;align-items:center;justify-content:center;text-align:center}
  .badge::before{content:"";position:absolute;inset:6px;border:1.5px dashed var(--white);border-radius:50%}
  .badge p{color:var(--white);font-size:9px;font-weight:700;line-height:11px;width:78px}
  .badge em{font-weight:900}

  .tag{position:absolute;height:20px;padding:0 18px 0 8px;background:var(--yellow-tag);font-family:"Oswald",sans-serif;font-size:17px;line-height:20px;color:var(--teal-dark);clip-path:polygon(0 0,100% 0,92% 50%,100% 100%,0 100%)}
  .tag--services{left:22px;top:195px;width:124px}
  .tag--certs{left:22px;top:290px;width:130px}

  .list{position:absolute;list-style:none;color:var(--white);font-size:10.2px;line-height:12.2px}
  .list li::before{content:"●";font-size:8px;margin-right:4px;vertical-align:1px}
  .list--services-a{left:32px;top:217px}
  .list--services-b{left:226px;top:217px}
  .list--certs-a{left:32px;top:312px}
  .list--certs-b{left:226px;top:312px}

  .footer{position:absolute;left:0;top:358px;width:538px;height:38px;background:var(--white)}
  .footer-item{position:absolute;top:4px}
  .footer-item small{display:block;font-size:7px;color:var(--grey-text)}
  .footer-item strong{display:flex;align-items:center;gap:3px;font-family:"Oswald",sans-serif;font-weight:500;font-size:15px;color:var(--blue-text);line-height:20px}
  .dot{width:14px;height:14px;border-radius:50%;background:var(--teal-dark);flex:none}
  .footer-item--web{left:30px}
  .footer-item--social{left:233px}
  .footer-item--phone{left:413px}
  .front-base{position:absolute;left:0;top:396px;width:538px;height:21px;background:linear-gradient(90deg,var(--teal-dark),var(--teal),var(--teal-dark))}

  /* back */
  .back-panel{position:absolute;left:0;top:0;width:261px;height:309px;background:var(--white)}
  .back-brand{position:absolute;left:0;top:12px;width:261px;text-align:center;font-family:"Oswald",sans-serif;font-weight:500;color:var(--teal);font-size:21px;line-height:26px}
  .back-tagline{position:absolute;left:0;top:38px;width:261px;font-size:10px}
  .back-photo{position:absolute;left:0;top:52px;width:261px;height:140px;background:linear-gradient(90deg,#d8b08a,#9a6b4a 40%,#e1c3a4 70%,#a77a58)}
  .back-waves{position:absolute;left:0;top:0}
  .offers{position:absolute;left:0;top:196px;width:261px;text-align:center;font-weight:900;font-size:10px;line-height:11.5px;letter-spacing:.1px}
  .offer{padding:3px 0 4px;border-bottom:1.5px dotted var(--yellow)}
  .offer:last-child{border-bottom:none}
  .offer--yellow{color:var(--yellow)}
  .offer--green{color:var(--green)}
  .contact{position:absolute;left:40px;top:312px;display:flex;align-items:center;gap:6px}
  .contact-label{font-size:10px;line-height:10px;color:var(--teal-dark);text-align:right}
  .contact-icon{width:26px;height:26px;border-radius:50%;background:var(--teal-dark);display:flex;align-items:center;justify-content:center}
  .contact-number{font-family:"Oswald",sans-serif;font-weight:500;font-size:22px;color:var(--teal)}
</style>
</head>
<body>

<section class="card card--front">
  <div class="front-photo" role="img" aria-label="Photo of a smiling teacher helping young children with schoolwork at a table"></div>
  <svg class="front-waves" width="538" height="417" viewBox="0 0 538 417" aria-hidden="true">
    <defs>
      <linearGradient id="frontBlue" x1="0" y1="0" x2="0" y2="1">
        <stop offset="0" stop-color="#1e8fae"/><stop offset="1" stop-color="#0e5b7c"/>
      </linearGradient>
    </defs>
    <path d="M0 135 C120 175 240 205 340 190 C430 176 500 140 538 118 L538 417 L0 417Z" fill="var(--green)"/>
    <path d="M0 150 C120 190 250 215 350 200 C440 186 505 150 538 130 L538 417 L0 417Z" fill="var(--yellow)"/>
    <path d="M0 156 C120 196 250 221 350 206 C440 192 505 158 538 138 L538 417 L0 417Z" fill="url(#frontBlue)"/>
  </svg>

  <div class="title-panel">
    <h1 class="brand">Hartwell Family Day Care</h1>
    <p class="tagline">home day care service</p>
    <p class="ages">For children 6 weeks to 12 years</p>
  </div>

  <div class="badge"><p>we accept <em>KVD</em>, <em>employer</em>, and <em>military assistance</em></p></div>

  <h2 class="tag tag--services">Our services</h2>
  <ul class="list list--services-a">
    <li>Open 24 hours.</li>
    <li>Saturday care available.</li>
    <li>3 meals and 3 snacks served daily.</li>
    <li>Small provider to student ratio.</li>
    <li>Kindergarten preparedness program.</li>
  </ul>
  <ul class="list list--services-b">
    <li>Tutoring, introduction to Spanish.</li>
    <li>After school program.</li>
    <li>NQBT membership.</li>
    <li>Transportation from and to home, school drop off and pick up.</li>
    <li>Camera surveillance system.</li>
  </ul>

  <h2 class="tag tag--certs">Certifications</h2>
  <ul class="list list--certs-a">
    <li>State of Ohio licensed</li>
    <li>First aid and CPR certified</li>
    <li>Health and safety training</li>
  </ul>
  <ul class="list list--certs-b">
    <li>14 years of combined experience</li>
    <li>QRU Bachelor of Science Degree</li>
  </ul>

  <footer class="footer">
    <div class="footer-item footer-item--web"><small>for more info visit us at:</small><strong><span class="dot"></span>HartwellFamilyDayCare.example</strong></div>
    <div class="footer-item footer-item--social"><small>follow us on:</small><strong><span class="dot"></span>Hartwell Family Day Care</strong></div>
    <div class="footer-item footer-item--phone"><small>Call for tour:</small><strong>
      <span class="dot" style="display:flex;align-items:center;justify-content:center">
        <svg width="9" height="9" viewBox="0 0 24 24"><path fill="#fff" d="M6.6 10.8a15 15 0 0 0 6.6 6.6l2.2-2.2c.3-.3.7-.4 1-.2 1.1.4 2.3.6 3.6.6.6 0 1 .4 1 1V20c0 .6-.4 1-1 1A17 17 0 0 1 3 4c0-.6.4-1 1-1h3.5c.6 0 1 .4 1 1 0 1.3.2 2.5.6 3.6.1.3 0 .7-.2 1z"/></svg>
      </span>555 271 9043</strong></div>
  </footer>
  <div class="front-base"></div>
</section>

<section class="card card--back">
  <div class="back-panel">
    <div class="back-photo" role="img" aria-label="Photo of four happy young children hugging each other"></div>
    <svg class="back-waves" width="261" height="309" viewBox="0 0 261 309" aria-hidden="true">
      <defs>
        <linearGradient id="backBlue" x1="0" y1="0" x2="0" y2="1">
          <stop offset="0" stop-color="#124f78"/><stop offset="1" stop-color="#0a3a5c"/>
        </linearGradient>
      </defs>
      <path d="M0 0 H261 V50 H0Z" fill="#fff"/>
      <path d="M0 140 C60 175 150 200 261 168 L261 309 L0 309Z" fill="var(--yellow)"/>
      <path d="M0 152 C70 188 160 206 261 180 L261 309 L0 309Z" fill="url(#backBlue)"/>
    </svg>
    <h1 class="back-brand">Hartwell Family Day Care</h1>
    <p class="tagline back-tagline">home day care service</p>
    <div class="offers">
      <p class="offer offer--yellow">FOR CHILDREN 6 WEEKS TO 12 YEARS</p>
      <p class="offer offer--green">LOWER PRICES QUALITY SERVICES</p>
      <p class="offer offer--yellow">PRESENT THIS POSTCARD FOR $30<br>PER CHILD REGISTRATION FEE WAIVER</p>
      <p class="offer offer--green">LOCATED NEAR LARKMOOR BLVD.<br>ASHFORD, OHIO 40000</p>
    </div>
  </div>
  <div class="contact">
    <p class="contact-label">CONTACT<br>INFO</p>
    <span class="contact-icon">
      <svg width="14" height="14" viewBox="0 0 24 24"><path fill="#fff" d="M6.6 10.8a15 15 0 0 0 6.6 6.6l2.2-2.2c.3-.3.7-.4 1-.2 1.1.4 2.3.6 3.6.6.6 0 1 .4 1 1V20c0 .6-.4 1-1 1A17 17 0 0 1 3 4c0-.6.4-1 1-1h3.5c.6 0 1 .4 1 1 0 1.3.2 2.5.6 3.6.1.3 0 .7-.2 1z"/></svg>
    </span>
    <span class="contact-number">555 271 9043</span>
  </div>
</section>

</body>
</html>
```